Professional and creatice Life Coach - Business Card design

I just relaunched my website and now i a need a correspoonding business card for my task as life coach. My website is www.dlorvan.net as reference. The compass is kind of a symbol for my work, as I help people navigate through their challenging phases in life. The business card should be colorful, but not too playful as I also adress business people. So it sould be creative, but professional (also to suport my other business as Management Consultant)

Target Market(s)

People who want to get teir problems resolved, in business, partnership and other personal realms

Industry/Entity Type

Life Coaching

Contact Information for Business Card

Front side should include Name, Phone number, Email, Website and address

Font styles to use
Sans Serif

Colors
add136

Requirements
Must have
• "Mag. Benedikt Haufmoll" -> Name
"Energetische Praxis" -> Jobtitle (describing my profession as life coach)
colours and style should match my website www.dlorvan.net
Nice to have
• a compass as a symbol

```html
<!DOCTYPE html>
<html lang="de">
<head>
<meta charset="utf-8">
<title>Benedikt Haufmoll – Visitenkarte</title>
<link rel="stylesheet" href="https://fonts.googleapis.com/css2?family=Exo+2:wght@600&family=Roboto:wght@400&display=swap">
<style>
  :root {
    --stage: #3b3b3d;
    --card: #1f1f21;
    --card-edge: #2a2a2d;
    --accent: #add136;
    --text: #f2f2f2;
    --muted: #d8d8d8;
    --emboss-dark: #2c2c2f;
    --emboss-light: #58585c;
  }
  * { box-sizing: border-box; margin: 0; padding: 0; }
  html, body {
    width: 799px; height: 1200px; overflow: hidden;
    background: var(--stage);
  }
  .stage {
    position: relative; width: 799px; height: 1200px;
    display: flex; flex-direction: column; align-items: center;
    justify-content: space-around; padding: 60px 0;
  }
  .card {
    position: relative; width: 600px; height: 350px;
    background: var(--card);
    border: 1px solid var(--card-edge);
    box-shadow: 0 14px 30px rgba(0,0,0,.45);
    overflow: hidden;
  }
  .card-front .emblem {
    position: absolute; left: 50%; top: 50%;
    width: 230px; height: 230px; margin: -115px 0 0 -115px;
    border-radius: 50%;
    background: radial-gradient(circle at 45% 40%, var(--emboss-light), var(--emboss-dark) 70%);
  }
  .card-back .identity {
    position: absolute; left: 36px; top: 34px;
  }
  .name {
    font-family: "Exo 2", sans-serif; font-weight: 600;
    font-size: 25px; color: var(--accent); letter-spacing: .2px;
  }
  .role {
    font-family: "Roboto", sans-serif; font-size: 15px;
    color: var(--muted); margin-top: 2px; letter-spacing: .3px;
  }
  .contacts {
    position: absolute; left: 36px; top: 196px;
    list-style: none;
    font-family: "Roboto", sans-serif; font-size: 16px; color: var(--text);
  }
  .contacts li {
    display: flex; align-items: center; gap: 10px; height: 23px;
  }
  .contacts svg { width: 13px; height: 13px; fill: var(--accent); flex: none; }
  .contacts .address { margin-left: -8px; margin-top: 4px; }
  .card-back .emblem {
    position: absolute; left: 330px; top: 105px;
    width: 230px; height: 230px; border-radius: 50%;
    background: radial-gradient(circle at 50% 50%, var(--accent) 0 45%, #7c963a 62%, #8d8d8d 64% 68%, var(--card) 69%);
  }
</style>
</head>
<body>
<main class="stage">
  <section class="card card-front">
    <div class="emblem" role="img" aria-label="Embossed compass rose symbol"></div>
  </section>

  <section class="card card-back">
    <header class="identity">
      <h1 class="name">Mag. Benedikt Haufmoll</h1>
      <p class="role">Energetische Praxis</p>
    </header>
    <ul class="contacts">
      <li>
        <svg viewBox="0 0 16 16" aria-hidden="true"><path d="M3 1h3l1.5 4-2 1.3a9 9 0 0 0 4.2 4.2l1.3-2 4 1.5v3a2 2 0 0 1-2 2A13 13 0 0 1 1 3a2 2 0 0 1 2-2z"/></svg>
        +43 660 4187392
      </li>
      <li>
        <svg viewBox="0 0 16 16" aria-hidden="true"><path d="M1 3h14v10H1z M1 3l7 6 7-6" stroke="#1f1f21" stroke-width="1.2"/></svg>
        benedikt@haufmoll.one
      </li>
      <li>
        <svg viewBox="0 0 16 16" aria-hidden="true"><circle cx="8" cy="8" r="7"/><path d="M1 8h14M8 1c3 3 3 11 0 14M8 1c-3 3-3 11 0 14" stroke="#1f1f21" stroke-width="1.1" fill="none"/></svg>
        www.dlorvan.net
      </li>
      <li class="address">Moosgasse 9, 5412 Fernau, Österreich</li>
    </ul>
    <div class="emblem" role="img" aria-label="Green compass rose symbol in a grey ring"></div>
  </section>
</main>
</body>
</html>
```